4th Generation Family Business Needs a New Card Design!

We are a family owned 4th Generation company. We are based in the Sydney, Australia area and we are desperately in need of a more modern and classy card. We are monumental masons who design, supply & erect lasting memorials throughout cemeteries in Sydney. Our customers are normally in a period of grieving. I have attached logo files that will need to be implemented on the card. Company was established 1935. Australian Owned and Operated. Card needs to be designed to PRINTLY.com specification.

Target Market(s)

Our target market is based upon people that a grieving for family members that have passed away. We also deal with alot of companies that own and operate cemeteries.

Industry/Entity Type

Business

Contact Information for Business Card

Oliver Brantley, Operations Manager, 0417552908, oliver@hollowaystoneworks.com.au
Martin Brantley, Director, 0431906627, martin@hollowaystoneworks.com.au
Phone # 02 9634 2258
Website: www.hollowaystoneworks.com.au
Address: Suite 17, 8 Calloway Lane, East Penrose, Sydney NSW 2290

Font styles to use
Serif
Decorative
Script

Requirements
Must have
• Would like to see the logo nicely implemented with a modern design. Embossed lettering would be a nice additive.

```html
<!DOCTYPE html>
<html lang="en">
<head>
<meta charset="utf-8">
<title>Holloway Stoneworks – Business Card</title>
<link rel="stylesheet" href="https://fonts.googleapis.com/css2?family=Cinzel:wght@400;600&family=Open+Sans:ital,wght@0,400;1,400&display=swap">
<style>
  :root {
    --backdrop: #8e8e8e;
    --paper: #ebebeb;
    --ink: #1f1f1f;
    --ink-soft: #4a4a4a;
    --gold: #c9a02c;
    --card-black: #141414;
    --reverse-ink: #ececec;
    --divider: #b9b9b9;
  }
  * { box-sizing: border-box; margin: 0; padding: 0; }
  html, body {
    width: 1105px; height: 1200px; overflow: hidden;
    background: var(--backdrop);
  }
  .canvas { position: relative; width: 1105px; height: 1200px; }
  .card {
    position: absolute; left: 182px; width: 746px; height: 425px;
  }
  .card--front { top: 119px; background: var(--paper); }
  .card--back { top: 637px; background: var(--card-black); }

  .brand {
    position: absolute;
    font-family: "Cinzel", serif; font-weight: 600;
    text-align: center; line-height: 1.12;
  }
  .card--front .brand {
    left: 40px; width: 300px; top: 150px;
    color: var(--ink); font-size: 40px;
  }
  .card--back .brand {
    left: 0; width: 746px; top: 128px;
    color: var(--reverse-ink); font-size: 48px;
  }
  .brand span { display: block; }
  .brand .brand__sub { font-size: 0.78em; letter-spacing: 0.02em; }

  .divider {
    position: absolute; left: 356px; top: 88px;
    width: 1px; height: 250px; background: var(--divider);
  }
  .details { position: absolute; left: 385px; top: 78px; color: var(--ink-soft); }
  .details__name {
    font-family: "Cinzel", serif; font-weight: 600;
    font-size: 28px; color: var(--ink); letter-spacing: 0.03em; line-height: 1.15;
  }
  .details__role {
    font-family: "Cinzel", serif; font-weight: 400;
    font-size: 19px; color: var(--gold); letter-spacing: 0.04em; margin-top: 2px;
  }
  .details__address {
    font-family: "Open Sans", sans-serif; font-size: 18px; line-height: 28px;
    margin-top: 14px;
  }
  .contact-list { list-style: none; margin-top: 14px; }
  .contact-list li {
    display: flex; align-items: center; height: 29px;
    font-family: "Open Sans", sans-serif; font-size: 18px;
  }
  .contact-list svg { width: 17px; height: 17px; margin: 0 10px 0 6px; fill: var(--ink); }

  .web-address {
    position: absolute; left: 0; width: 746px; top: 358px; text-align: center;
    font-family: "Open Sans", sans-serif; font-style: italic;
    font-size: 20px; letter-spacing: 0.1em; color: var(--reverse-ink);
  }
</style>
</head>
<body>
<main class="canvas">

  <section class="card card--front">
    <div class="brand"><span>Holloway</span><span class="brand__sub">Stoneworks</span></div>
    <div class="divider"></div>
    <div class="details">
      <h1 class="details__name">Oliver Brantley</h1>
      <p class="details__role">Operations Manager</p>
      <p class="details__address">Suite 17, 8 Calloway Lane<br>East Penrose, Sydney NSW 2290</p>
      <ul class="contact-list">
        <li><svg viewBox="0 0 24 24" aria-hidden="true"><path d="M6.6 10.8a15.1 15.1 0 0 0 6.6 6.6l2.2-2.2a1 1 0 0 1 1-.25 11.4 11.4 0 0 0 3.6.57 1 1 0 0 1 1 1V20a1 1 0 0 1-1 1A17 17 0 0 1 3 4a1 1 0 0 1 1-1h3.5a1 1 0 0 1 1 1c0 1.25.2 2.45.57 3.57a1 1 0 0 1-.25 1z"/></svg>02 9634 2258</li>
        <li><svg viewBox="0 0 24 24" aria-hidden="true"><path d="M7 1h10a2 2 0 0 1 2 2v18a2 2 0 0 1-2 2H7a2 2 0 0 1-2-2V3a2 2 0 0 1 2-2zm0 3v14h10V4zm5 15.5a1.2 1.2 0 1 0 0 2.4 1.2 1.2 0 0 0 0-2.4z"/></svg>0417552908</li>
        <li><svg viewBox="0 0 24 24" aria-hidden="true"><path d="M2 5h20v14H2zm2 2v.5l8 5 8-5V7l-8 5z"/></svg>oliver@hollowaystoneworks.com.au</li>
        <li><svg viewBox="0 0 24 24" aria-hidden="true"><path d="M12 2a10 10 0 1 0 0 20 10 10 0 0 0 0-20zm-1 17.9A8 8 0 0 1 4.1 11H7c.1 3 1.6 6.3 4 8.9zM7 9H4.3A8 8 0 0 1 11 4.1C8.7 6 7.3 7.5 7 9zm6 10.9c1.9-2.4 3.1-5.6 3.2-8.9h3.7a8 8 0 0 1-6.9 8.9zM16.2 9C16 7 15 5.5 13 4.1A8 8 0 0 1 19.7 9z"/></svg>www.hollowaystoneworks.com.au</li>
      </ul>
    </div>
  </section>

  <section class="card card--back">
    <div class="brand"><span>Holloway</span><span class="brand__sub">Stoneworks</span></div>
    <p class="web-address">www.hollowaystoneworks.com.au</p>
  </section>

</main>
</body>
</html>
```